Email Signiture and letterhead design

we are looking for a modern business design to incorporate our logo and qel certification plus social icons for Vorlant, Pelmora, and zandoro
they must include our UK vat and also company registration as text but I can fill these out. Email signature to have a link/icon to our webshop www.trexolan.co.uk

Target Market(s)

All

Font styles to use
Serif
Sans Serif

Requirements
Must have
• Address, tel, email , web details incorperated
Nice to have
• a professional looking letter head and email signiture, Email signature to have a link/icon to our webshop www.trexolan.co.uk

```html
<!DOCTYPE html>
<html lang="en">
<head>
<meta charset="utf-8">
<title>Trexolan Axles Ltd – Letterhead and Email Signature</title>
<link href="https://fonts.googleapis.com/css2?family=Roboto:wght@300;400;500;700&display=swap" rel="stylesheet">
<style>
  :root{
    --stage:#8a8a8a;
    --paper:#f7f4f5;
    --red:#e41e26;
    --charcoal:#3d3d3f;
    --ink:#4a4a4a;
    --body:#555555;
    --label:#f2f2f2;
  }
  *{box-sizing:border-box;margin:0;padding:0}
  html,body{width:1200px;height:873px;overflow:hidden}
  body{background:var(--stage);font-family:"Roboto",Arial,sans-serif;position:relative;color:var(--ink)}

  .sheet{position:absolute;background:var(--paper);box-shadow:0 2px 8px rgba(0,0,0,.25);overflow:hidden}
  .letterhead{left:51px;top:70px;width:524px;height:739px}
  .signature{left:644px;top:351px;width:486px;height:137px}

  .caption{position:absolute;color:var(--label);font-size:13px;transform:translateX(-50%);white-space:nowrap}
  .caption-letterhead{left:277px;top:826px}
  .caption-signature{left:886px;top:512px}

  .social{position:absolute;display:flex;gap:3px}
  .social span{width:15px;height:15px;border-radius:50%;background:var(--red);display:block}
  .letterhead .social{left:457px;top:14px}

  .brand{position:absolute;display:flex;align-items:center;gap:6px;color:var(--red);font-weight:500;letter-spacing:.3px;white-space:nowrap}
  .brand .mark{width:22px;height:22px;border-radius:50%;background:var(--red);flex:none}
  .letterhead .brand{left:39px;top:96px;font-size:17px}
  .signature .brand{left:31px;top:44px;font-size:13px}
  .signature .brand .mark{width:16px;height:16px}

  .contact{position:absolute;font-weight:300;font-size:10px;line-height:12.7px;color:var(--ink);white-space:nowrap}
  .contact svg{width:9px;height:9px;fill:var(--red);flex:none;display:block}
  .letterhead .contact{left:371px;top:62px}
  .contact .phone{display:flex;align-items:center;gap:5px;margin-bottom:6px}

  .salutation{position:absolute;left:39px;top:207px;font-size:15px;font-weight:400;color:var(--ink)}
  .letter-body{position:absolute;left:39px;top:250px;width:437px;font-size:8.3px;line-height:12.6px;color:var(--body);text-align:justify}
  .letter-body p{margin-bottom:12.6px}
  .closing{position:absolute;left:39px;top:517px;font-size:8.5px;color:var(--body)}
  .sign-mark{position:absolute;left:50px;top:553px;width:68px;height:29px;background:linear-gradient(90deg,#d9d6d8,#e8e5e7);border-radius:3px}
  .signer{position:absolute;left:55px;top:609px}
  .signer .name{font-size:12px;color:var(--ink)}
  .signer .role{font-size:9px;color:var(--body);margin-top:3px}

  .footer-band{position:absolute;left:0;bottom:0;width:524px;height:54px}
  .footer-url{position:absolute;right:48px;bottom:22px;font-size:9px;font-weight:700;letter-spacing:1.4px;color:#1f1f1f}
  .footer-url em{font-style:normal;color:var(--red)}

  .signature .contact{right:28px;top:28px;text-align:right;line-height:13px}
  .signature .contact div{display:flex;align-items:center;justify-content:flex-end;gap:8px}
  .signature .registered{position:absolute;left:31px;top:84px;font-weight:300;font-size:10.3px;line-height:13px;color:var(--ink);white-space:nowrap}
  .sig-band{position:absolute;left:0;bottom:0;width:486px;height:56px}
  .signature .social{left:410px;top:105px}
</style>
</head>
<body>

<section class="sheet letterhead" aria-label="Letterhead">
  <div class="social" aria-label="Vorlant, zandoro and Pelmora"><span></span><span></span><span></span></div>

  <div class="brand"><span class="mark"></span>Trexolan Axles Ltd</div>

  <div class="contact">
    <div class="phone"><svg viewBox="0 0 24 24"><path d="M6.6 10.8a15.1 15.1 0 0 0 6.6 6.6l2.2-2.2a1 1 0 0 1 1-.25 11.4 11.4 0 0 0 3.6.57 1 1 0 0 1 1 1V20a1 1 0 0 1-1 1A17 17 0 0 1 3 4a1 1 0 0 1 1-1h3.5a1 1 0 0 1 1 1c0 1.25.2 2.45.57 3.57a1 1 0 0 1-.25 1z"/></svg>+44 (0) 161 555 0182</div>
    <div>VAT - ABC-1A2345</div>
    <div>Fernhill Street North,</div>
    <div>Aldersby,</div>
    <div>Manchester, M99 4QT</div>
  </div>

  <div class="salutation">Dear Mr. Hale,</div>

  <div class="letter-body">
    <p>Lorem ipsum dolor sit amet, consectetur adipiscing elit. Donec orci purus, luctus vitae dignissim eu, iaculis sed purus. Vivamus faucibus, ipsum nec aliquet viverra, leo mauris condimentum ligula, sit amet sagittis enim ligula quis arcu. Nam egestas tortor id nisi porttitor mattis. In tortor ante, ultricies in suscipit a, tempus non massa. Vivamus et auctor mi. Fusce vel massa nulla. Phasellus nec eros mauris, et scelerisque orci.</p>
    <p>Donec malesuada orci vitae nulla accumsan porta a id massa. Quisque accumsan iaculis magna sit amet fringilla. Maecenas consequat, magna eget tincidunt semper, odio nibh rutrum mi, id feugiat ante nisi eu risus. Vestibulum nunc orci, rhoncus a placerat in, ultricies in mi. Cras mattis varius eros, vel fringilla nisi suscipit eget. Quisque scelerisque sagittis nulla at porttitor.</p>
    <p>Sed id augue vitae urna euismod commodo aliquet a quam. Pellentesque arcu velit, cursus et malesuada ut, consequat et diam. Nullam erat sem, rhoncus id ullamcorper vitae, rhoncus et arcu. In ultricies ultricies nulla, ut rutrum nisi iaculis at. Donec eu magna a metus ornare faucibus. Fusce aliquet faucibus ultricies. Morbi semper, est id tincidunt gravida, sem arcu adipiscing lacus, ac bibendum nulla leo eu purus. Quisque nec diam sed risus consectetur a ccumsan quis quis nibh. Vestibulum id purus lorem.</p>
    <p>It is a long established fact that a reader will be distracted by the readable content of a page when looking at its layout. The point of using Lorem Ipsum is that it has a more-or-less normal distribution of letters, as opposed to using 'Content here, content here', making it look like readable English. Many desktop publishing packages</p>
  </div>

  <div class="closing">Sincerely,</div>
  <div class="sign-mark" role="img" aria-label="Handwritten signature"></div>
  <div class="signer">
    <div class="name">Daniel Marsh</div>
    <div class="role">CEO/ Founder</div>
  </div>

  <svg class="footer-band" viewBox="0 0 524 54" aria-hidden="true">
    <rect x="389" y="0" width="135" height="54" fill="var(--charcoal)"/>
    <path d="M380 0 L389 0 C455 0 488 14 488 30 C488 44 478 52 470 54 L380 54 Z" fill="var(--paper)"/>
  </svg>
  <div class="footer-url">www.<em>trexolan</em>.co.uk</div>
</section>
<div class="caption caption-letterhead">Letterhead_01</div>

<section class="sheet signature" aria-label="Email signature">
  <div class="brand"><span class="mark"></span>Trexolan Axles Ltd</div>

  <div class="contact">
    <div>+44 (0) 161 555 0182 <svg viewBox="0 0 24 24"><path d="M6.6 10.8a15.1 15.1 0 0 0 6.6 6.6l2.2-2.2a1 1 0 0 1 1-.25 11.4 11.4 0 0 0 3.6.57 1 1 0 0 1 1 1V20a1 1 0 0 1-1 1A17 17 0 0 1 3 4a1 1 0 0 1 1-1h3.5a1 1 0 0 1 1 1c0 1.25.2 2.45.57 3.57a1 1 0 0 1-.25 1z"/></svg></div>
    <div>www.trexolan.co.uk <svg viewBox="0 0 24 24"><circle cx="12" cy="12" r="11"/><path d="M8 7h6l-3 4h4l-7 6 2-5H7z" fill="var(--paper)"/></svg></div>
  </div>

  <div class="registered">
    <div>VAT - ABC-1A2345</div>
    <div>Fernhill Street North,</div>
    <div>Aldersby, Manchester, M99 4QT</div>
  </div>

  <svg class="sig-band" viewBox="0 0 486 56" aria-hidden="true">
    <rect x="289" y="0" width="197" height="56" fill="var(--charcoal)"/>
    <path d="M280 0 L289 0 C350 0 390 16 390 34 C390 46 380 54 375 56 L280 56 Z" fill="var(--paper)"/>
  </svg>
  <div class="social" aria-label="Vorlant, zandoro and Pelmora"><span></span><span></span><span></span></div>
</section>
<div class="caption caption-signature">Email Signature</div>

</body>
</html>
```